Velcor Prime Brochure for Chemicals Products

We need a bifold A3 brochure for the exhibition.
you can visit our company website (www.velcorprime.com) for more information about our company.
Company logo and color code attached.
The brochure should contain brief introduction of company, industries, product, and contact (address , telephone and email; joral.k@velcorprime.com)

Product Portfolio:
1. Intermediates
2. Plastics
3. Rubber
4. Additive
5. Fiber
Detail of each products portfolio are in the website. we would like to add product detail but you may help to design how to put it beautifully.

Target Market(s)

Our customers are factories in related industry.

Industry/Entity Type

Automotive, Paint, Electrical Appliance, Tyre and footwear, Textile, Animal Feed, Lubricant

Font styles to use
Sans Serif

Requirements
Must have
• Logo, Product Portfolio for different market.
Nice to have
• prefer curve design rather than rectangular

```html
<!DOCTYPE html>
<html lang="en">
<head>
<meta charset="utf-8">
<title>Velcor Prime – Product Portfolio</title>
<link href="https://fonts.googleapis.com/css2?family=Montserrat:wght@400;500;600&family=Poppins:wght@800&display=swap" rel="stylesheet">
<style>
  :root {
    --page-bg: #ffffff;
    --circle-outer: #d7ecf8;
    --label-green: #abcf22;
    --body-blue: #1a7cc0;
    --footer-blue: #0289d4;
    --brand-panel: #eaf5fc;
    --white: #ffffff;
  }
  * { margin: 0; padding: 0; box-sizing: border-box; }
  html, body { width: 849px; height: 1200px; overflow: hidden; background: var(--page-bg); }
  .page { position: relative; width: 849px; height: 1200px; overflow: hidden; background: var(--page-bg); }
  .backdrop { position: absolute; inset: 0; }

  .portfolio-item { position: absolute; left: 34px; width: 540px; height: 143px; }
  .product-photo {
    position: absolute; left: 0; top: 0; width: 254px; height: 143px;
    border-radius: 8px;
  }
  .photo-paint { background: linear-gradient(135deg, #f08a1c 0%, #7b2fd0 25%, #1ed6c8 50%, #f5c400 70%, #e0184a 85%, #c9d92a 100%); }
  .photo-pellets { background: linear-gradient(120deg, #e6b89c 0%, #d9a98b 30%, #8fcbe0 55%, #7cc3dc 100%); }
  .photo-bands { background: linear-gradient(120deg, #f4f0ea 0%, #e9f1f2 45%, #f1b6c8 70%, #f7e6a2 85%, #eeece6 100%); }
  .photo-lab { background: linear-gradient(160deg, #5c4a3a 0%, #e9e6e2 35%, #cfa772 70%, #b8874f 100%); }
  .photo-yarn { background: linear-gradient(150deg, #2b4f9a 0%, #3a63b5 40%, #1f3b7a 75%, #13264f 100%); }

  .brand-panel {
    position: absolute; left: 0; top: 0; width: 254px; height: 143px;
    border-radius: 8px; background: var(--brand-panel);
    display: flex; align-items: center; justify-content: center; gap: 10px;
  }
  .brand-mark { width: 26px; height: 26px; border-radius: 50%; background: var(--label-green); }
  .brand-name {
    font-family: "Montserrat", sans-serif; font-weight: 600; font-size: 24px;
    color: var(--body-blue); letter-spacing: 0.2px;
  }

  .category-label {
    position: absolute; left: 254px; top: 10px; width: 274px; height: 34px;
    background: var(--label-green);
    border-radius: 0 14px 14px 0;
    display: flex; align-items: center; justify-content: center;
    font-family: "Poppins", sans-serif; font-weight: 800; font-size: 16.5px;
    color: var(--white); letter-spacing: 0.1px; white-space: nowrap;
  }
  .category-text {
    position: absolute; left: 264px; top: 56px; width: 282px;
    font-family: "Montserrat", sans-serif; font-size: 7.3px; line-height: 9.6px;
    color: var(--body-blue);
  }

  .contact-band {
    position: absolute; left: 0; top: 1073px; width: 849px; height: 127px;
    background: var(--footer-blue);
  }
  .contact-dot { position: absolute; left: 32px; top: 1092px; width: 21px; height: 21px; border-radius: 50%; background: var(--label-green); }
  .contact-title { position: absolute; left: 73px; top: 1087px; font-size: 20px; font-weight: 500; color: var(--white); font-family: "Montserrat", sans-serif; letter-spacing: 0.3px; }
  .contact-rule { position: absolute; left: 229px; top: 1106px; width: 585px; height: 1px; background: var(--white); }
  .contact-item {
    position: absolute; top: 1126px; width: 210px; margin-left: -105px;
    text-align: center; font-family: "Montserrat", sans-serif; font-size: 13px; font-weight: 500; color: var(--white);
    line-height: 16px;
  }
  .contact-item svg { display: block; margin: 0 auto 8px; height: 26px; }
  .contact-item.address { font-size: 10.5px; line-height: 13px; }
</style>
</head>
<body>
<div class="page">
  <svg class="backdrop" width="849" height="1200" viewBox="0 0 849 1200" aria-hidden="true">
    <defs>
      <linearGradient id="innerCircle" x1="0" y1="0" x2="0" y2="1">
        <stop offset="0" stop-color="#b7e2f7"/>
        <stop offset="1" stop-color="#9ac9e2"/>
      </linearGradient>
    </defs>
    <circle cx="893" cy="545" r="527" fill="#d7ecf8"/>
    <circle cx="874" cy="566" r="417" fill="url(#innerCircle)"/>
  </svg>

  <section class="portfolio-item about" style="top:28px">
    <div class="brand-panel">
      <span class="brand-mark"></span>
      <span class="brand-name">Velcor Prime</span>
    </div>
    <h2 class="category-label">ABOUT VELCOR PRIME</h2>
    <p class="category-text">Velcor Prime is a trusted supplier of chemicals, plastics, rubber, additives and fibers to factories across Asia. We serve automotive, paint, electrical appliance, tyre and footwear, textile, animal feed and lubricant industries with reliable quality and technical support.</p>
  </section>

  <section class="portfolio-item" style="top:196px">
    <div class="product-photo photo-paint" role="img" aria-label="Open paint cans filled with bright colours"></div>
    <h2 class="category-label">CHEMICALS &amp; INTERMEDIATES</h2>
    <p class="category-text">Our chemicals range from intermediates, monomer, and other products bringing synergy to our client. We offer products to coating resin, ink, adhesive, polyurethane, lubricants, polymer polymerization, textile auxiliaries, etc.</p>
  </section>

  <section class="portfolio-item" style="top:364px">
    <div class="product-photo photo-pellets" role="img" aria-label="Hand holding light blue plastic pellets"></div>
    <h2 class="category-label">PLASTICS</h2>
    <p class="category-text">We offer polymer and compound materials including short glass fiber, long glass fiber, mineral fillers, conductive, flame retardant, magnetic compound, carbon fiber, color compound and other customs compound.</p>
  </section>

  <section class="portfolio-item" style="top:532px">
    <div class="product-photo photo-bands" role="img" aria-label="Ball of colourful rubber bands on a white table"></div>
    <h2 class="category-label">RUBBER</h2>
    <p class="category-text">We supply synthetic rubber to major tire producers as well as rubber compounder and converter.</p>
  </section>

  <section class="portfolio-item" style="top:700px">
    <div class="product-photo photo-lab" role="img" aria-label="Lab technician pouring blue powder into a mixing bowl"></div>
    <h2 class="category-label">ADDITIVES</h2>
    <p class="category-text">We provide wide product range of additives for plastics compound, rubber compound, coating, modified starch and animal feed. We also offer additive masterbatch used for packaging industries.</p>
  </section>

  <section class="portfolio-item" style="top:867px">
    <div class="product-photo photo-yarn" role="img" aria-label="Rows of blue yarn cones"></div>
    <h2 class="category-label">FIBERS</h2>
    <p class="category-text">We offer specialties staple fiber and filament yarn for nonwoven, textile spinning, flooring, abrasives, tire cord, and protection fabric. The functionalized products such as antibacteria, flame retardant, biodegradable fiber are also available.</p>
  </section>

  <footer>
    <div class="contact-band"></div>
    <div class="contact-dot"></div>
    <h3 class="contact-title">Contact Now</h3>
    <div class="contact-rule"></div>

    <div class="contact-item" style="left:120px">
      <svg viewBox="0 0 24 24" width="26" aria-hidden="true"><path fill="#fff" d="M6.6 2.5c.6-.4 1.4-.3 1.8.3l2.2 3.2c.4.6.3 1.3-.2 1.8L9 9.2c1 2.3 3.5 4.8 5.8 5.8l1.4-1.4c.5-.5 1.2-.6 1.8-.2l3.2 2.2c.6.4.7 1.2.3 1.8l-1.4 2c-.9 1.2-2.5 1.6-3.9 1C9.9 18 6 14.1 3.6 7.8c-.6-1.4-.2-3 1-3.9z"/></svg>
      +66-82-4190576
    </div>
    <div class="contact-item" style="left:325px">
      <svg viewBox="0 0 30 22" width="30" aria-hidden="true"><rect x="1" y="1" width="28" height="20" fill="none" stroke="#fff" stroke-width="2"/><path d="M1 1l14 11L29 1M1 21l10-9M29 21l-10-9" fill="none" stroke="#fff" stroke-width="2"/></svg>
      joral.k@velcorprime.com
    </div>
    <div class="contact-item address" style="left:530px">
      <svg viewBox="0 0 24 24" width="26" aria-hidden="true"><path fill="#fff" d="M12 1.5c-4.1 0-7.4 3.3-7.4 7.4 0 5.3 7.4 13.6 7.4 13.6s7.4-8.3 7.4-13.6c0-4.1-3.3-7.4-7.4-7.4zm0 10.2a2.8 2.8 0 1 1 0-5.6 2.8 2.8 0 0 1 0 5.6z"/></svg>
      27 Lumen Tower, Sathorn,<br>Bangkok 10120
    </div>
    <div class="contact-item" style="left:730px">
      <svg viewBox="0 0 24 24" width="26" aria-hidden="true"><g fill="none" stroke="#fff" stroke-width="1.6"><circle cx="12" cy="12" r="10.5"/><ellipse cx="12" cy="12" rx="4.5" ry="10.5"/><path d="M1.5 12h21M3.5 6.5h17M3.5 17.5h17"/></g></svg>
      www.velcorprime.com
    </div>
  </footer>
</div>
</body>
</html>
```